Venture Capital Investment Firm

We are looking to overhaul our existing website (substantially), with only using the same logos (which we can provide).
We are an investment firm that focuses on making loans to late stage technology companies. Our site should ultimately look like other venture capital firms, and look modern and fresh. We have an existing website www.northvaleloan.com which this will be replacing, although we will be using a lot of the existing written content, and potentially the numbers of pages we will need, we are not wed to anything else. Please feel free to shoot any questions at any time and thank you in advance for your help!
Websites we like as examples:
https://www.tkbrandel.com/
https://www.emberwoodfunds.com/
Target Market(s)
Potential investors who will invest in our firm, as well as potentially companies that are looking to borrow money from us.

```html
<!DOCTYPE html>
<html lang="en">
<head>
<meta charset="utf-8">
<title>Northvale Capital — Structured Credit Investment</title>
<link rel="stylesheet" href="https://fonts.googleapis.com/css2?family=Montserrat:wght@300;400;500;600;700&family=Open+Sans:wght@400;600&display=swap">
<style>
:root{
  --navy:#1d1938;
  --navy-deep:#15122b;
  --ink:#222033;
  --text:#5d5b6a;
  --muted:#8a8898;
  --paper:#ffffff;
  --mist:#f1f1f4;
  --lavender:#d9d5ec;
  --blue:#2e3fd3;
  --line:#d8d8de;
}
*{box-sizing:border-box;margin:0;padding:0}
html,body{width:1200px;height:3390px;overflow:hidden}
body{position:relative;background:var(--paper);font-family:"Open Sans",Arial,sans-serif;color:var(--text);font-size:12px;line-height:1.7}
h1,h2,h3,h4,.brand,.nav a,.btn,.eyebrow{font-family:"Montserrat",Arial,sans-serif}
.abs{position:absolute}

/* hero */
.hero{position:absolute;left:0;top:0;width:1200px;height:600px;overflow:hidden}
.hero-photo{position:absolute;inset:0;background:linear-gradient(180deg,#2a2750 0%,#3b2a4e 45%,#4a2b3e 75%,#1b1733 100%)}
.hero-shade{position:absolute;inset:0;background:linear-gradient(90deg,rgba(21,18,43,.75) 0%,rgba(21,18,43,.25) 60%,rgba(21,18,43,.5) 100%)}
.brand{display:flex;align-items:center;gap:12px;color:#fff;font-weight:500;font-size:24px;letter-spacing:.5px;line-height:1.2}
.brand-dot{width:30px;height:30px;border-radius:50%;border:3px solid currentColor}
.brand small{display:block;font-size:7px;letter-spacing:1.5px;font-weight:500;margin-top:2px}
.hero .brand{left:38px;top:22px}
.nav{position:absolute;top:36px;right:38px;display:flex;align-items:center;gap:30px}
.nav a{color:#fff;text-decoration:none;font-size:11px;font-weight:500;letter-spacing:.5px}
.nav .home{width:14px;height:12px}
.nav .login{background:#fff;color:var(--navy);padding:7px 10px;font-size:10px;font-weight:600}
.hero-copy{left:160px;top:236px;color:#fff}
.hero-copy h1{font-size:28px;font-weight:600;line-height:1.35}
.hero-copy p{font-size:12px;line-height:1.6;margin-top:8px;font-style:italic}
.btn{display:inline-block;font-size:10px;font-weight:600;letter-spacing:.5px;text-decoration:none;padding:8px 12px;white-space:nowrap}
.btn-ghost{border:1.5px solid #fff;color:#fff}
.btn-dark{background:var(--navy);color:#fff}
.btn-outline{border:1.5px solid var(--navy);color:var(--navy);background:#fff}
.hero-copy .btn{margin-top:18px}
.pager{right:30px;top:268px;color:#fff;font-family:"Montserrat",sans-serif;font-size:10px;line-height:2.4;text-align:right}
.pager span{display:block;opacity:.7}
.pager .on{opacity:1;font-weight:600}

/* what we do */
.eyebrow{font-size:10px;font-weight:500;letter-spacing:1px;color:var(--ink);text-transform:uppercase}
.what{left:160px;top:655px;width:430px}
.what h2{font-size:29px;font-weight:400;color:var(--ink);line-height:1.3;margin:12px 0 22px}
.what p{margin-bottom:12px;font-size:11px}
.pillar{border-left:3px solid var(--navy);padding-left:18px;margin:18px 0 0}
.pillar h3{font-size:16px;font-weight:500;color:var(--ink);margin-bottom:6px;text-transform:uppercase}
.what .btn{margin-top:28px}
.growth-art{left:620px;top:780px;width:390px;height:370px;background:linear-gradient(160deg,#f4f4f6 0%,#e4e4ea 40%,#5a67e0 75%,#2e3fd3 100%);border-radius:4px}

/* team */
.team{position:absolute;left:0;top:1230px;width:1200px;height:840px;background:var(--navy);clip-path:polygon(0 70px,100% 0,100% 715px,0 838px)}
.section-label{display:flex;align-items:center;justify-content:center;gap:14px}
.section-label::before,.section-label::after{content:"";width:34px;height:1px;background:currentColor}
.team .section-label{position:absolute;top:132px;left:0;width:1200px;color:#fff}
.team h2{position:absolute;top:156px;left:0;width:1200px;text-align:center;color:#fff;font-size:27px;font-weight:400}
.card{position:absolute;top:235px;width:280px;height:470px;background:#fff;border:3px solid #fff;text-align:center}
.card-head{height:120px;background:linear-gradient(180deg,#2a2549,#3b3564);color:#fff;font-family:"Montserrat",sans-serif;font-weight:600;font-size:14px;padding-top:16px}
.portrait{width:176px;height:176px;border-radius:50%;background:linear-gradient(180deg,var(--lavender),#c7c1e2);margin:-70px auto 0;position:relative}
.socials{display:flex;justify-content:center;gap:8px;margin-top:-14px;position:relative}
.socials i{width:22px;height:22px;border-radius:50%;background:var(--navy);border:2px solid #fff}
.card h4{font-size:22px;font-weight:500;color:var(--ink);margin-top:4px;line-height:1.4}
.card .role{font-family:"Montserrat",sans-serif;font-size:10px;font-weight:500;letter-spacing:.5px;color:var(--ink)}
.card p{font-size:10px;line-height:1.6;margin:10px 22px 0}
.more{display:inline-flex;align-items:center;gap:6px;margin-top:14px;font-family:"Montserrat",sans-serif;font-size:9px;font-weight:700;color:var(--ink)}

/* about */
.about-bg{position:absolute;left:0;top:2030px;width:1200px;height:1030px;background:var(--mist);z-index:-1}
.about-name{left:160px;top:2200px;width:360px;text-align:center;font-family:"Montserrat",sans-serif;font-size:44px;font-weight:500;line-height:1.2;color:var(--navy)}
.about{left:536px;top:2085px;width:505px}
.about h2{font-size:27px;font-weight:400;color:var(--ink);margin-top:10px}
.about h3{font-size:16px;font-weight:500;color:var(--ink);margin:8px 0 16px}
.about p{font-size:10.5px;margin-bottom:18px}
.about .btn{margin-top:2px}
.rule{left:160px;top:2548px;width:880px;height:1px;background:var(--line)}

/* news */
.news-label{left:0;top:2602px;width:1200px;color:var(--ink)}
.news-title{left:0;top:2626px;width:1200px;text-align:center;font-size:27px;font-weight:400;color:var(--ink);text-transform:uppercase}
.news-card{position:absolute;top:2708px;width:430px;height:278px;background:#fff;padding:22px 24px 0 86px}
.date{position:absolute;left:16px;top:22px;width:52px;height:52px;border-radius:50%;background:var(--navy);color:#fff;text-align:center;font-family:"Montserrat",sans-serif;font-size:8px;line-height:1.2;padding-top:10px}
.date b{display:block;font-size:12px}
.news-card h4{font-size:17px;font-weight:600;color:var(--ink);line-height:1.3}
.news-card em{display:block;font-size:10px;margin:6px 0 8px}
.news-card p{font-size:10px;line-height:1.65}
.news-card .btn{position:absolute;left:50%;bottom:-16px;transform:translateX(-50%);padding:7px 24px}
.btn-soft{background:#d6d6de;color:var(--ink)}
.arrow{position:absolute;top:2828px;width:28px;height:28px;border-radius:50%;display:flex;align-items:center;justify-content:center}
.arrow.prev{left:146px;background:#fff}
.arrow.next{left:1026px;background:var(--navy)}

/* footer */
.to-top{left:550px;top:3040px;width:100px;text-align:center;font-family:"Montserrat",sans-serif;font-size:7px;font-weight:700;color:var(--ink);line-height:1.2;white-space:nowrap}
.to-top i{display:flex;align-items:center;justify-content:center;width:28px;height:28px;margin:0 auto 6px;border-radius:50%;background:var(--navy)}
.footer .brand{left:160px;top:3128px;color:var(--navy)}
.address{left:160px;top:3196px;font-size:10px;color:var(--ink);line-height:1.5}
.address strong{font-family:"Montserrat",sans-serif;font-size:11px;display:block}
.address .line{display:flex;gap:8px}
.address .mail{margin-top:12px;font-family:"Montserrat",sans-serif;font-weight:600;font-size:10px}
.links{left:534px;top:3126px;list-style:none;font-family:"Montserrat",sans-serif;font-size:10px;font-weight:600;color:var(--ink);line-height:2.95}
.links li::before{content:"";display:inline-block;width:10px;height:1px;background:var(--ink);vertical-align:middle;margin-right:8px}
.signup{left:760px;top:3126px;width:280px}
.signup h4,.follow h4{font-size:11px;font-weight:700;color:var(--ink);text-transform:uppercase}
.field{margin-top:10px;height:38px;background:var(--navy);color:#fff;font-size:10px;display:flex;align-items:center;justify-content:space-between;padding:0 12px;font-family:"Montserrat",sans-serif}
.follow{left:760px;top:3236px}
.follow div{display:flex;gap:10px;margin-top:8px}
.follow i{width:12px;height:12px;border-radius:50%;background:var(--navy)}
.base{left:160px;top:3346px;width:880px;border-top:1px solid var(--line);padding-top:14px;font-size:9px;color:var(--ink)}
</style>
</head>
<body>

<header class="hero">
  <div class="hero-photo" role="img" aria-label="Dusk skyline of downtown high-rise towers under a violet sky"></div>
  <div class="hero-shade"></div>
  <div class="brand abs"><span class="brand-dot"></span><span>Northvale Capital<small>NORTHVALE CAPITAL PARTNERS, LLC</small></span></div>
  <nav class="nav">
    <svg class="home" viewBox="0 0 14 12"><path d="M7 0 0 6h2v6h4V8h2v4h4V6h2z" fill="#fff"/></svg>
    <a href="#">STRATEGY</a><a href="#">MEET THE TEAM</a><a href="#">ABOUT</a><a href="#">NEWS</a><a href="#">CONTACT</a>
    <a class="login" href="#">INVESTOR LOGIN</a>
  </nav>
  <div class="hero-copy abs">
    <h1>Northvale Capital Started<br>with a big idea</h1>
    <p>We are a global structured credit investment firm focused<br>on the healthcare and technology industries</p>
    <a class="btn btn-ghost" href="#">CONTACT US</a>
  </div>
  <div class="pager abs"><span class="on">01</span><span>02</span><span>03</span></div>
</header>

<section class="what abs">
  <div class="eyebrow">What we do</div>
  <h2>We provide flexible capital to innovative companies and their investors</h2>
  <p>Our focus spans the life science and technology industries, two sectors where intellectual property (IP) is an integral driver of asset and enterprise value.</p>
  <p>Our broad experience in investing, technology evaluation, and product forecasting affords us a unique understanding of the value of assets in these dynamic sectors, allowing us to see value where others cannot.</p>
  <div class="pillar"><h3>Life Sciences</h3><p>We have a long track record of partnering with companies and investors that create and commercialize life science products, with extensive experience spanning biopharmaceuticals, medical devices, and tools &amp; diagnostics.</p></div>
  <div class="pillar"><h3>Technology</h3><p>We uniquely offer sizeable and flexible structured credit financing solutions to innovative technology companies, with a focus on enterprise software, data &amp; analytics, semiconductors, and communications systems.</p></div>
  <a class="btn btn-dark" href="#">VIEW DETAILED STRATEGY</a>
</section>
<div class="growth-art abs" role="img" aria-label="Illustration of an investor holding a coin beside stacked coins, a rising arrow and a blue bar chart"></div>

<section class="team">
  <div class="section-label eyebrow">Meet our team</div>
  <h2>Senior Team</h2>
  <article class="card" style="left:160px">
    <div class="card-head">Life Sciences, Technology</div>
    <div class="portrait" role="img" aria-label="Portrait photo of Marcus Ellery"></div>
    <div class="socials"><i></i><i></i></div>
    <h4>Marcus Ellery</h4><div class="role">MANAGING PARTNER</div>
    <p>Marcus Ellery is an industry leader with over $1.2B in structured credit investments since 2004, leading origination and underwriting.</p>
    <div class="more">→ READ MORE</div>
  </article>
  <article class="card" style="left:460px">
    <div class="card-head">Technology</div>
    <div class="portrait" role="img" aria-label="Portrait photo of Daniel Okafor"></div>
    <div class="socials"><i></i><i></i></div>
    <h4>Daniel Okafor</h4><div class="role">MANAGING PARTNER</div>
    <p>Daniel Okafor leads technology investment origination and evaluation at Northvale, with over 15 years of transaction experience.</p>
    <div class="more">→ READ MORE</div>
  </article>
  <article class="card" style="left:760px">
    <div class="card-head">Chief Operating Officer</div>
    <div class="portrait" role="img" aria-label="Portrait photo of Simon Hartley"></div>
    <div class="socials"><i></i><i></i></div>
    <h4>Simon Hartley</h4><div class="role">PARTNER</div>
    <p>Simon Hartley serves as Chief Operating Officer at Northvale, with 20 years of experience in alternative investment operations.</p>
    <div class="more">→ READ MORE</div>
  </article>
</section>

<div class="about-bg"></div>
<div class="about-name abs">Northvale<br>Capital</div>
<section class="about abs">
  <div class="eyebrow" style="display:flex;align-items:center;gap:10px"><span style="width:30px;height:1px;background:var(--ink)"></span>Who we are</div>
  <h2>About Us</h2>
  <h3>Finance proven innovation with a different approach</h3>
  <p>Northvale Capital is a private investment firm unique in its dual focus on life science and technology credit opportunities. Our entrepreneurial approach to investing reflects a broad recognition and appreciation for the critical role intellectual property plays in the successful commercialization of products. We apply our extensive industry expertise to assess the revenue visibility created by these assets and offer a range of creative financing solutions.</p>
  <p>A pioneer in providing life science structured credit beginning in 2004, the Northvale team was the first to introduce flexible structured credit to the technology sector in 2014. Our team was also early to recognize the potential of "non-core" assets beyond drug royalties, acquiring over $300M of branded generics offering predictable cash flows from large pharmaceutical firms and partnering with entrepreneurial teams to successfully manage these brands.</p>
  <a class="btn btn-outline" href="#">KNOW MORE ABOUT US</a>
</section>
<div class="rule abs"></div>

<div class="news-label section-label eyebrow abs">News updates</div>
<h2 class="news-title abs">Northvale News</h2>
<a class="arrow prev" href="#"><svg width="8" height="10" viewBox="0 0 8 10"><path d="M6 1 2 5l4 4" stroke="#1d1938" stroke-width="2" fill="none"/></svg></a>
<article class="news-card" style="left:160px">
  <div class="date">20<b>April</b>'18</div>
  <h4>Northvale completes structured debt investment in BrightLoop</h4>
  <em>Press Release</em>
  <p>Northvale Capital Partners ("Northvale") announced today that it has completed a structured debt investment in BrightLoop, Inc. ("BrightLoop"), the leader in employee communication. The financing will be used to advance BrightLoop's continued growth as the SaaS company scales its Pulse Suite software. BrightLoop is headquartered in Redwood City, California.</p>
  <a class="btn btn-dark" href="#">READ MORE</a>
</article>
<article class="news-card" style="left:610px">
  <div class="date">19<b>Oct.</b>'16</div>
  <h4>Northvale completes $22,000,000 structured debt investment in Formwell</h4>
  <em>Press Release</em>
  <p>Northvale Capital Partners ("Northvale") announced today that it has completed a $22,000,000 structured debt investment in Formwell AS ("Formwell"). Formwell, headquartered in Oslo, Norway, is Europe's leading supplier of Software-as-a-Service (SaaS) solutions for Enterprise Feedback.</p>
  <a class="btn btn-soft" href="#">READ MORE</a>
</article>
<a class="arrow next" href="#"><svg width="8" height="10" viewBox="0 0 8 10"><path d="M2 1l4 4-4 4" stroke="#fff" stroke-width="2" fill="none"/></svg></a>

<footer class="footer">
  <div class="to-top abs"><i><svg width="10" height="8" viewBox="0 0 10 8"><path d="M1 6l4-4 4 4" stroke="#fff" stroke-width="2" fill="none"/></svg></i>BACK TO TOP</div>
  <div class="brand abs"><span class="brand-dot"></span><span>Northvale Capital<small>NORTHVALE CAPITAL PARTNERS, LLC</small></span></div>
  <div class="address abs">
    <div class="line"><svg width="12" height="16" viewBox="0 0 12 16"><path d="M6 0a6 6 0 0 0-6 6c0 4.5 6 10 6 10s6-5.5 6-10a6 6 0 0 0-6-6zm0 8.5A2.5 2.5 0 1 1 6 3.5a2.5 2.5 0 0 1 0 5z" fill="#1d1938"/></svg>
      <div><strong>SAN FRANCISCO</strong>2140 HARLOW STREET #318<br>SAN FRANCISCO, CA 94107</div></div>
    <div class="line mail"><svg width="14" height="11" viewBox="0 0 14 11"><rect x=".5" y=".5" width="13" height="10" fill="none" stroke="#1d1938"/><path d="M.5 .5 7 6l6.5-5.5" fill="none" stroke="#1d1938"/></svg>INQUIRIES@NORTHVALECAP.COM</div>
  </div>
  <ul class="links abs"><li>HOME</li><li>STRATEGY</li><li>MEET THE TEAM</li><li>ABOUT</li><li>NEWS</li><li>CONTACT</li></ul>
  <div class="signup abs"><h4>Sign up for newsletter</h4>
    <div class="field">ENTER EMAIL ADDRESS<svg width="12" height="12" viewBox="0 0 12 12"><path d="M0 5 12 0 7 12 5.5 6.5z" fill="#fff"/></svg></div></div>
  <div class="follow abs"><h4>Follow us</h4><div><i></i><i></i><i></i></div></div>
  <div class="base abs">© 2020 Northvale Capital Partners, LLC. All Rights Reserved. | Legal Disclaimer</div>
</footer>

</body>
</html>
```